Business card design needed

I run a life coaching business.
I coach individuals, businesses & groups.
Our aim is create massive change for our clients.
I would like to see a card that is inspirational, something that provokes the thought of achieving your personal best.
Be your own inspiration is a phrase I am considering using.

Target Market(s)

People who are looking to create a massive change in their lives.

Industry/Entity Type

Life Coaching

Contact Information for Business Card

Summit Stride Coaching
Neil Corbett
Head Coach
email neil@velomira.com.au
Mob 0412 583 604

Logo styles of interest
Abstract Logo
Requirements
Must have
• I wouldlike to have a free introductory offer on the reverse side of the card.
It would read something like:
Is coaching for me/you?
Try a free 45 minute session.
Book now call or email for your appointment.

```html
<!DOCTYPE html>
<html lang="en">
<head>
<meta charset="utf-8">
<title>Summit Stride Coaching – Business Card Options</title>
<link rel="stylesheet" href="https://fonts.googleapis.com/css2?family=Alfa+Slab+One&family=Open+Sans:wght@400;600;700&display=swap">
<style>
  :root {
    --navy: #3a3287;
    --orange: #f0821e;
    --ink: #222222;
    --grey-text: #3c3c3c;
    --board: #ebeced;
    --card: #ffffff;
    --art-light: #d9dcec;
    --art-mid: #8f93c4;
    --art-gold: #c9a73a;
  }
  * { margin: 0; padding: 0; box-sizing: border-box; }
  html, body { width: 1200px; height: 747px; overflow: hidden; }
  body {
    position: relative;
    background: var(--board);
    font-family: "Open Sans", Arial, sans-serif;
  }
  .option-number {
    position: absolute;
    font-size: 20px;
    color: var(--ink);
  }
  .card {
    position: absolute;
    width: 528px;
    height: 302px;
    background: var(--card);
    box-shadow: 0 3px 10px rgba(0,0,0,0.18);
    overflow: hidden;
  }
  .card > * { position: absolute; }

  /* Option 1 */
  .slab-title {
    left: 0; right: 0;
    text-align: center;
    font-family: "Alfa Slab One", Georgia, serif;
    color: var(--orange);
    text-shadow: 1px 1px 0 #5a2a08, -1px 0 0 #5a2a08, 0 -1px 0 #5a2a08;
    letter-spacing: 0.5px;
  }
  .front-1 .slab-title { top: 34px; font-size: 27px; }
  .back-1 .slab-title { top: 46px; font-size: 26px; }
  .front-1 .person-name { left: 101px; top: 91px; font-size: 21px; font-weight: 700; color: var(--navy); }
  .front-1 .person-role { left: 102px; top: 119px; font-size: 16px; color: var(--navy); }
  .front-1 .contact { left: 80px; font-size: 20px; font-weight: 700; color: var(--navy); display: flex; align-items: center; gap: 6px; }
  .front-1 .contact svg { fill: none; stroke: var(--orange); stroke-width: 1.6; }
  .front-1 .contact-phone { top: 156px; }
  .front-1 .contact-email { top: 186px; }
  .front-1 .key-art { left: 354px; top: 92px; width: 126px; height: 145px; }
  .back-1 .offer { left: 0; right: 0; text-align: center; font-weight: 700; color: var(--ink); }
  .back-1 .offer-main { top: 120px; font-size: 18px; }
  .back-1 .offer-note { top: 189px; font-size: 15px; }
  .corner-band { left: 0; bottom: 0; width: 528px; height: 30px; }

  /* Option 2 */
  .header-bar {
    left: 0; top: 0; width: 100%; height: 68px;
    background: var(--navy);
    color: #fff;
    font-weight: 600;
    font-size: 29px;
    letter-spacing: 1px;
    text-align: center;
    line-height: 68px;
  }
  .stripe-band {
    left: 0; bottom: 6px; width: 100%; height: 14px;
    background: repeating-linear-gradient(-60deg, var(--navy) 0 14px, #fff 14px 17px);
  }
  .front-2 .key-art { left: 22px; top: 100px; width: 138px; height: 158px; }
  .front-2 .person-name { left: 208px; top: 107px; font-size: 26px; font-weight: 700; color: var(--navy); }
  .front-2 .person-role { left: 208px; top: 143px; font-size: 20px; color: var(--grey-text); letter-spacing: 0.5px; }
  .front-2 .contact { left: 182px; font-size: 20px; color: var(--grey-text); display: flex; align-items: center; gap: 6px; }
  .front-2 .contact svg { fill: none; stroke: var(--navy); stroke-width: 1.6; }
  .front-2 .contact-phone { top: 189px; }
  .front-2 .contact-email { top: 220px; }
  .back-2 .offer { left: 0; right: 0; text-align: center; font-weight: 700; color: var(--navy); }
  .back-2 .offer-main { top: 121px; font-size: 19px; }
  .back-2 .offer-note { top: 188px; font-size: 16px; }

  .key-art {
    border-radius: 8px;
    background: radial-gradient(circle at 65% 25%, var(--art-gold) 0 12%, transparent 13%),
                linear-gradient(160deg, var(--art-light), var(--art-mid));
    opacity: 0.9;
  }
</style>
</head>
<body>
  <span class="option-number" style="left:36px; top:44px;">1</span>
  <span class="option-number" style="left:611px; top:34px;">2</span>

  <!-- Option 1 front -->
  <section class="card front-1" style="left:66px; top:44px;">
    <h1 class="slab-title">SUMMIT STRIDE COACHING</h1>
    <p class="person-name">Neil Corbett</p>
    <p class="person-role">Head Coach</p>
    <p class="contact contact-phone">
      <svg width="16" height="16" viewBox="0 0 16 16"><path d="M4 1.5l2.2 3-1.4 1.6c.9 2 2.4 3.5 4.4 4.4l1.6-1.4 3 2.2-1.3 2.6C7 13.5 2.5 9 1.6 3z"/></svg>
      0412 583 604
    </p>
    <p class="contact contact-email">
      <svg width="18" height="14" viewBox="0 0 18 14"><rect x="1" y="2" width="16" height="10"/><path d="M1 2l8 6 8-6"/></svg>
      neil@velomira.com.au
    </p>
    <div class="key-art" role="img" aria-label="Illustration of a gold key turning in a jigsaw puzzle piece"></div>
    <svg class="corner-band" viewBox="0 0 528 30" aria-hidden="true">
      <polygon points="0,6 218,6 250,16 528,16 528,30 0,30" fill="var(--orange)"/>
      <polygon points="244,4 528,4 528,13 272,13" fill="var(--navy)"/>
    </svg>
  </section>

  <!-- Option 2 front -->
  <section class="card front-2" style="left:640px; top:42px; height:303px;">
    <h1 class="header-bar">SUMMIT STRIDE COACHING</h1>
    <div class="key-art" role="img" aria-label="Illustration of a gold key turning in a jigsaw puzzle piece"></div>
    <p class="person-name">Neil Corbett</p>
    <p class="person-role">Head Coach</p>
    <p class="contact contact-phone">
      <svg width="16" height="16" viewBox="0 0 16 16"><path d="M4 1.5l2.2 3-1.4 1.6c.9 2 2.4 3.5 4.4 4.4l1.6-1.4 3 2.2-1.3 2.6C7 13.5 2.5 9 1.6 3z"/></svg>
      0412 583 604
    </p>
    <p class="contact contact-email">
      <svg width="18" height="14" viewBox="0 0 18 14"><rect x="1" y="2" width="16" height="10"/><path d="M1 2l8 6 8-6"/></svg>
      neil@velomira.com.au
    </p>
    <div class="stripe-band"></div>
  </section>

  <!-- Option 1 back -->
  <section class="card back-1" style="left:68px; top:412px;">
    <h2 class="slab-title">IS COACHING FOR YOU?</h2>
    <p class="offer offer-main">Try a free 45 minute session</p>
    <p class="offer offer-note">Book now, call or email for your appointment</p>
    <svg class="corner-band" viewBox="0 0 528 30" aria-hidden="true">
      <polygon points="0,6 287,6 310,0 528,0 528,30 0,30" fill="var(--orange)"/>
      <polygon points="0,0 304,0 282,12 0,12" fill="var(--navy)"/>
      <polygon points="0,12 282,12 288,20 0,20" fill="#fff"/>
    </svg>
  </section>

  <!-- Option 2 back -->
  <section class="card back-2" style="left:641px; top:406px;">
    <h2 class="header-bar">IS COACHING FOR YOU?</h2>
    <p class="offer offer-main">Try a free 45 minute session</p>
    <p class="offer offer-note">Book now, call or email for your appointment</p>
    <div class="stripe-band" style="bottom:2px;"></div>
  </section>
</body>
</html>
```